New web design for a service provider in the medical field

We are looking for a new design for our website. We are a company that repairs and sells medical endoscopes. Our customers include doctors and hospitals. Our current website can be found at https://lumenfix.example/en/lumenfix-english.
We need a new web design (without programming) for the following 3 pages:
-Startpage https://lumenfix.example/en/lumenfix-english/
-Used endoscopes https://lumenfix.example/en/used-endoscopes/
-Purchase https://lumenfix.example/en/purchase/
The design should be modern and stylish.
The blue color of the logo should be reflected on the page, but not too intrusive.
I have uploaded the images from the header. If more images are needed, let me know and I will upload them.

Target Market(s)
Doctors and hospitals

```html
<!DOCTYPE html>
<html lang="en">
<head>
<meta charset="utf-8">
<title>LumenFix – Used devices</title>
<link href="https://fonts.googleapis.com/css2?family=Montserrat:wght@300;400;500;600;700;800&display=swap" rel="stylesheet">
<style>
:root{
  --navy:#0b1f6b;
  --navy-dark:#0a1b5c;
  --blue:#0a3fb0;
  --royal:#1446c4;
  --cyan:#12c2ec;
  --sky:#2fa9f5;
  --grey-band:#ececec;
  --card-grey:#ebebeb;
  --text:#6d6f78;
  --text-dark:#2a2d3a;
  --white:#ffffff;
}
*{box-sizing:border-box;margin:0;padding:0}
html,body{width:1200px;height:4858px;overflow:hidden}
body{font-family:"Montserrat",sans-serif;color:var(--text-dark);background:var(--white);position:relative}
.abs{position:absolute}
a{color:inherit;text-decoration:none}

/* header */
.brand{left:120px;top:62px;font-size:22px;font-weight:700;color:var(--navy);display:flex;align-items:center;gap:10px}
.brand .dot{width:14px;height:14px;border-radius:50%;background:var(--sky)}
.topbar{top:28px;right:52px;display:flex;align-items:center;gap:34px;font-size:11px;color:var(--text)}
.topbar span{display:flex;align-items:center;gap:8px}
.nav{top:116px;right:60px;display:flex;gap:50px;font-size:13.5px;font-weight:500;color:var(--navy)}
.nav .active{border-bottom:2px solid var(--navy);padding-bottom:4px}

/* hero */
.hero{left:0;top:175px;width:1200px;height:233px;background:var(--grey-band)}
.hero-photo{right:0;top:0;width:600px;height:233px;background:linear-gradient(100deg,var(--grey-band) 0%,#dadbdf 35%,#3a3d45 70%,#d8d9dc 100%)}
.crumb{left:128px;top:20px;font-size:11px;color:#8a8c93}
.crumb b{color:var(--sky);font-weight:400}
.hero h1{left:123px;top:120px;font-size:44px;font-weight:800;color:var(--navy)}
.hero p{left:124px;top:176px;font-size:25px;font-weight:400;color:var(--navy)}

/* tabs */
.tabs{top:463px;left:174px;display:flex;align-items:center;font-size:13px;color:var(--navy);font-weight:500}
.tabs .tab{padding:0 28px;height:44px;line-height:44px}
.tabs .on{background:var(--cyan);border-radius:8px;padding:0 26px}

/* product cards */
.card{left:64px;width:1069px;height:376px;background:var(--card-grey)}
.card .photo{position:absolute;right:0;top:0;width:532px;height:376px}
.card h2{position:absolute;left:76px;top:44px;font-size:25px;font-weight:400;color:var(--navy)}
.card .sub{position:absolute;left:78px;top:80px;font-size:14px;color:var(--text-dark)}
.card .desc{position:absolute;left:78px;top:136px;width:370px;font-size:12px;line-height:16px;color:var(--text)}
.card .btn{position:absolute;left:76px;width:384px;height:30px;border-radius:15px;background:var(--navy);color:var(--white);font-size:12px;font-weight:700;letter-spacing:1px;text-align:center;line-height:30px}
.card .btn::after{content:"→";position:absolute;right:16px;font-weight:400}
.brands{position:absolute;left:78px;display:flex;gap:18px}
.brands span{width:106px;height:42px;border-radius:10px;background:#dcdcde;display:flex;align-items:center;justify-content:center;font-size:14px;font-weight:700;color:var(--navy-dark)}

/* purchase */
.purchase h2{left:125px;top:2372px;font-size:44px;font-weight:800;color:var(--navy)}
.rule{height:5px;width:80px;background:var(--cyan);border-radius:3px}
.copy{font-size:13px;line-height:21px;color:var(--text)}
.warranty-badge{left:128px;top:2706px;width:270px;height:70px;background:linear-gradient(90deg,var(--navy),var(--royal));border-radius:4px}
.quality{left:125px;top:2814px;font-size:24px;color:var(--navy)}
.btn-navy{height:30px;border-radius:15px;background:var(--navy);color:var(--white);font-size:12px;font-weight:700;letter-spacing:1px;text-align:center;line-height:30px}
.side-photo{left:808px;top:2706px;width:260px;height:407px;background:linear-gradient(160deg,#d9dbe0 0%,#f2f2f2 40%,#4a5470 75%,#cfd3dc 100%)}

/* why us */
.why{left:0;top:3190px;width:1200px;height:930px;background:linear-gradient(160deg,#0d2fa0 0%,#0a3cb3 50%,#0d4dc4 100%);overflow:hidden}
.why h2{position:absolute;left:125px;top:90px;font-size:44px;font-weight:800;color:var(--white)}
.why .rule{position:absolute;left:127px;top:155px}
.feature{position:absolute;width:330px;text-align:center;color:var(--white)}
.feature h3{font-size:24px;font-weight:400;margin-bottom:14px}
.feature p{font-size:12.5px;line-height:16.5px;width:230px;margin:0 auto;opacity:.92}

/* contact */
.help{top:4190px;width:500px;text-align:center}
.help h2{font-size:35px;font-weight:700;color:var(--text-dark);margin-top:34px}
.help p{font-size:12.5px;line-height:16px;color:var(--text);margin-top:22px;letter-spacing:.5px}
.pill{top:4460px;width:466px;height:40px;border-radius:20px;background:var(--sky);color:var(--white);font-size:10px;font-weight:700;text-align:center;line-height:40px;box-shadow:0 6px 12px rgba(47,169,245,.35)}
.divider{left:601px;top:4255px;width:2px;height:235px;background:var(--sky)}

/* footer */
.foot-brand{left:0;width:1200px;top:4610px;text-align:center;font-size:16px;font-weight:700;color:var(--navy)}
.socials{top:4700px;left:562px;display:flex;gap:24px}
.socials i{width:10px;height:10px;border-radius:50%;background:var(--navy)}
.flags{top:4738px;left:561px;display:flex;gap:34px;align-items:center}
.foot-links{top:4792px;left:0;width:1200px;display:flex;justify-content:center;gap:22px;font-size:9px;color:var(--text)}
.cert{left:1085px;top:4776px;width:52px;height:30px;background:#1b4fb0;border-radius:3px}
.copyright{left:0;top:4836px;width:1200px;height:22px;background:#e8e8e8;font-size:9px;line-height:22px;text-align:center;color:var(--text)}
</style>
</head>
<body>

<header>
  <div class="abs brand"><span class="dot"></span>LumenFix</div>
  <div class="abs topbar">
    <span>
      <svg width="12" height="9" viewBox="0 0 12 9"><rect x=".5" y=".5" width="11" height="8" fill="none" stroke="#8a8c93"/><path d="M.5 .5 6 5 11.5 .5" fill="none" stroke="#8a8c93"/></svg>
      info@lumenfix.example
    </span>
    <span>
      <svg width="10" height="10" viewBox="0 0 10 10"><path d="M2 0 4 2.5 3 4a6 6 0 0 0 3 3l1.5-1L10 8 8.5 10C4 10 0 6 0 1.5Z" fill="#8a8c93"/></svg>
      +49 000 555 0100
    </span>
    <span>
      <svg width="24" height="14" viewBox="0 0 24 14"><rect width="24" height="14" fill="#c8102e"/><rect y="2" width="24" height="2" fill="#fff"/><rect y="6" width="24" height="2" fill="#fff"/><rect y="10" width="24" height="2" fill="#fff"/><rect width="10" height="8" fill="#1c2f7a"/></svg>
    </span>
  </div>
  <nav class="abs nav">
    <a class="active" href="https://lumenfix.example/en/lumenfix-english/">Home</a>
    <a href="https://lumenfix.example/en/used-endoscopes/">Buy Used Endoscopes</a>
    <a href="https://lumenfix.example/en/purchase/">Sell Your Endoscope</a>
    <a href="#">• Other</a>
  </nav>
</header>

<section class="abs hero">
  <div class="abs hero-photo" role="img" aria-label="Photo of a video endoscope control body and processor unit"></div>
  <div class="abs crumb"><b>Home</b> / Used Endoscpes</div>
  <h1 class="abs">Used devices</h1>
  <p class="abs">Fair price – Full performances</p>
</section>

<div class="abs tabs">
  <span class="tab on">Flexible video endoscopes</span>
  <span class="tab">Processores and light-sources</span>
  <span class="tab">Endoscopy systems</span>
  <span class="tab">Accesories</span>
</div>

<section class="abs card" style="top:564px">
  <h2>+ Flexible video endoscopes</h2>
  <div class="sub">with warranty</div>
  <p class="desc">Discover our flexible endoscopes from the best brands such as Veyra, Kestrel and Marlow: gastroscopes, coloscopes, bronchoscopes, duodenoscopes, cystoscopes and more.</p>
  <a class="btn" style="top:233px">ALL BRANDS</a>
  <div class="brands" style="top:290px"><span>KESTREL</span><span>MARLOW</span><span>VEYRA</span></div>
  <div class="photo" role="img" aria-label="Photo of flexible endoscopes hanging on a wall rack" style="background:linear-gradient(90deg,#dfe1e6,#f4f4f6 30%,#2a2c33 55%,#e6e7ea 75%,#30323a 90%,#dcdde2)"></div>
</section>

<section class="abs card" style="top:1013px">
  <h2>+ Processores and light-sources</h2>
  <div class="sub">with warranty</div>
  <p class="desc">Provide better diagnosis to your patients by means of high-resolution imaging, implemented by the best video processors of the latest generation.</p>
  <a class="btn" style="top:233px">ALL BRANDS</a>
  <div class="brands" style="top:290px"><span>KESTREL</span><span>MARLOW</span><span>VEYRA</span></div>
  <div class="photo" role="img" aria-label="Photo of endoscopy video processor and light source front panels" style="background:linear-gradient(150deg,#f3f0ee,#d9d6d6 35%,#1d2029 60%,#c7532f 85%,#e7e5e5)"></div>
</section>

<section class="abs card" style="top:1464px">
  <h2>+ &nbsp;Endoscopy systems</h2>
  <div class="sub">with warranty</div>
  <p class="desc">We help you with configuring a complete endoscopy system for your needs and requirements - from the endoscope to the peripheral devices (processor, light source, screen, suction pump, etc.).</p>
  <a class="btn" style="top:240px">ALL ABOUT ENDOSCOPY-SYSTEMS!</a>
  <div class="photo" role="img" aria-label="Photo of a clinician at an endoscopy tower with monitor" style="background:linear-gradient(100deg,#e4e5e8,#6c7080 30%,#f1f1f2 55%,#dfe0e4 75%,#9aa3b8)"></div>
</section>

<section class="abs card" style="top:1908px">
  <h2>+ &nbsp;Accesories</h2>
  <div class="sub">with warranty</div>
  <p class="desc">We help you with configuring a complete endoscopy system for your needs and requirements - from the endoscope to the peripheral devices (processor, light source, screen, suction pump, etc.).</p>
  <a class="btn" style="top:240px">FIND YOUR ACCESSORIES HERE!</a>
  <div class="photo" role="img" aria-label="Photo of endoscope and accessories on a turquoise surgical drape" style="background:linear-gradient(160deg,#f0c67a,#7fc3cf 35%,#3aa3b2 60%,#22323a 80%,#4fb0bd)"></div>
</section>

<section class="purchase">
  <h2 class="abs">Purchase of used endoscopes</h2>
  <div class="abs rule" style="left:127px;top:2443px"></div>
  <p class="abs copy" style="left:128px;top:2516px;width:960px">Used endoscopes are an excellent, high-quality alternative to new equipment for all doctors and hospitals who want to add to their equipment pool cost-effectively. On our website you will find all types of equipment - gastroscopes, coloscopes, bronchoscopes, cystoscopes and duodenoscopes.</p>
  <p class="abs copy" style="left:128px;top:2598px;width:960px">All used endoscopes that we offer for sale were already in medical use and have been professionally looked after and serviced during this time. In addition, we can offer you endoscopy accessories both for medical examinations and for cleaning and maintaining your endoscopes.</p>

  <div class="abs warranty-badge" role="img" aria-label="Twelve months warranty badge"></div>
  <h3 class="abs quality" style="font-weight:400">Quality with warranty for more safety</h3>
  <p class="abs copy" style="left:128px;top:2860px;width:530px">After the purchase, our technicians subjected the devices to extensive technical tests and overhauled them. Last but not least, we rely on well-known brands that themselves stand for a high quality standard – Veyra, Kestrel and Marlow. For these reasons we can offer a twelve month warranty on our used equipment!</p>
  <p class="abs copy" style="left:128px;top:2984px;width:530px">Only tested quality leaves our company: To ensure the highest quality standards, we carry out an intensive outgoing inspection on every device before dispatch. We enclose documentation of the test result with your endoscope and archive it for future reference.</p>
  <a class="abs btn-navy" style="left:128px;top:3090px;width:306px">CONTACT US</a>
  <div class="abs side-photo" role="img" aria-label="Photo of a clinician holding an endoscope beside an endoscopy tower"></div>
</section>

<section class="abs why">
  <h2>Why Us?</h2>
  <div class="rule"></div>
  <div class="feature" style="left:99px;top:306px"><h3>Cost Efficient</h3><p>Our regular stock includes refurbished gastroscopes, coloscopes, bronchoscopes, cystoscopes and duodenoscopes from the well-known manufacturers Veyra, Kestrel and Marlow.</p></div>
  <div class="feature" style="left:424px;top:306px"><h3>No Maintenance Contract</h3><p>Our regular stock includes refurbished gastroscopes, coloscopes, bronchoscopes, cystoscopes and duodenoscopes from the well-known manufacturers Veyra, Kestrel and Marlow.</p></div>
  <div class="feature" style="left:809px;top:306px"><h3>German Quality</h3><p>Our regular stock includes refurbished gastroscopes, coloscopes, bronchoscopes, cystoscopes and duodenoscopes from the well-known manufacturers Veyra.</p></div>
  <div class="feature" style="left:99px;top:600px"><h3>Cost Efficient</h3><p>Our regular stock includes refurbished gastroscopes, coloscopes, bronchoscopes, cystoscopes and duodenoscopes from the well-known manufacturers Veyra, Kestrel and Marlow.</p></div>
  <div class="feature" style="left:424px;top:600px"><h3>No Maintenance Contract</h3><p>Our regular stock includes refurbished gastroscopes, coloscopes, bronchoscopes, cystoscopes and duodenoscopes from the well-known manufacturers Veyra, Kestrel and Marlow.</p></div>
  <div class="feature" style="left:809px;top:600px"><h3>German Quality</h3><p>Our regular stock includes refurbished gastroscopes, coloscopes, bronchoscopes, cystoscopes and duodenoscopes from the well-known manufacturers Veyra.</p></div>
</section>

<section>
  <div class="abs help" style="left:63px">
    <svg width="50" height="36" viewBox="0 0 50 36"><rect x="1" y="1" width="48" height="34" fill="none" stroke="#d2d3d6" stroke-width="2"/><path d="M1 1 25 20 49 1M1 35 19 16M49 35 31 16" fill="none" stroke="#d2d3d6" stroke-width="2"/></svg>
    <h2>We'll help you!</h2>
    <p>Discover classic and brand new styles in a variety of<br>shapes, colours and materials, from signature Frame<br>to the latest teardrop inspired watches.</p>
  </div>
  <div class="abs divider"></div>
  <div class="abs help" style="left:647px">
    <svg width="50" height="44" viewBox="0 0 50 44"><path d="M6 2 14 12 10 17a24 24 0 0 0 12 12l5-4 10 8-5 8C14 41 0 27 0 8Z" fill="#d2d3d6"/><path d="M32 20a8 8 0 0 1 6 8M34 12a16 16 0 0 1 12 16" fill="none" stroke="#d2d3d6" stroke-width="2.5"/></svg>
    <h2 style="margin-top:28px">Call Us</h2>
    <p>+49 000 555 0100</p>
    <p style="margin-top:10px">Monday - Friday<br>8AM - 20AM UTC</p>
  </div>
  <a class="abs pill" style="left:80px">CONTACT US</a>
  <a class="abs pill" style="left:665px">CALL NOW</a>
</section>

<footer>
  <div class="abs foot-brand">LumenFix</div>
  <div class="abs socials"><i></i><i></i><i></i></div>
  <div class="abs flags">
    <svg width="24" height="14" viewBox="0 0 24 14"><rect width="24" height="5" fill="#111"/><rect y="5" width="24" height="4" fill="#d00"/><rect y="9" width="24" height="5" fill="#ffce00"/></svg>
    <svg width="24" height="14" viewBox="0 0 24 14"><rect width="24" height="14" fill="#c8102e"/><rect y="2" width="24" height="2" fill="#fff"/><rect y="6" width="24" height="2" fill="#fff"/><rect y="10" width="24" height="2" fill="#fff"/><rect width="10" height="8" fill="#1c2f7a"/></svg>
  </div>
  <nav class="abs foot-links">
    <a href="https://lumenfix.example/en/lumenfix-english/">Home</a><a>Repair</a><a href="https://lumenfix.example/en/used-endoscopes/">Buy</a><a href="https://lumenfix.example/en/purchase/">Sell</a><a>pick-up order</a><a>about us</a><a>contact us</a>
  </nav>
  <div class="abs cert"></div>
  <div class="abs copyright">Copyright © 2022 LumenFix GmbH. Use of this website constitutes acceptance of our User Agreement and Privacy Policy.</div>
</footer>

</body>
</html>
```